New hardcover book cover

I want a striking, eye-catching cover with title, subtitle and a picture.See for previous book covers: www.brightmaplepress.com

Target Market(s)

young, successful entrepreneurs that have built a business in a niche market that they discovered.

Font styles to use
Serif

Colors

Designer to choose colors to be used in the design.

Requirements
Must have
• A book cover that impresses and captures the imagination of those who look at it.
• MY MISTAKE, SORRY.
• Title: Founders Behind the Quiet Trade Boom
• Subtitle: 25 stories of success from
• discovering hidden opportunities
• Author: Dorian Pelham
• Please use the photo attached, thanks.

```html
<!DOCTYPE html>
<html lang="en">
<head>
<meta charset="utf-8">
<title>Founders Behind the Quiet Trade Boom — Dorian Pelham</title>
<link rel="stylesheet" href="https://fonts.googleapis.com/css2?family=Raleway:wght@300;400;500&display=swap">
<style>
  :root {
    --ink-white: #ffffff;
    --target-red: #c8253f;
    --target-dark: #1c1d26;
    --steel: #5d6878;
    --sky: #9fc3dc;
    --sky-light: #d9e8f1;
    --base-slate: #2d3440;
  }
  html, body {
    margin: 0;
    padding: 0;
    width: 764px;
    height: 1200px;
    overflow: hidden;
    background: var(--target-dark);
  }
  .cover {
    position: relative;
    width: 764px;
    height: 1200px;
    overflow: hidden;
    font-family: "Raleway", sans-serif;
    color: var(--ink-white);
  }
  .cover-photo {
    position: absolute;
    inset: 0;
    background:
      radial-gradient(ellipse 60% 42% at 12% 44%, var(--target-red) 0%, #8d1a2f 45%, rgba(28,29,38,0) 80%),
      linear-gradient(100deg, var(--target-dark) 0%, #2a2b36 38%, var(--steel) 62%, var(--sky) 82%, var(--sky-light) 100%);
  }
  .cover-photo::after {
    content: "";
    position: absolute;
    inset: 0;
    background: linear-gradient(180deg, rgba(45,52,64,0) 45%, rgba(45,52,64,0.75) 70%, var(--base-slate) 100%);
  }
  .author {
    position: absolute;
    top: 30px;
    left: 0;
    right: 0;
    margin: 0;
    text-align: center;
    font-weight: 400;
    font-size: 31px;
    letter-spacing: 7px;
    text-transform: uppercase;
  }
  .title {
    position: absolute;
    top: 722px;
    left: 0;
    right: 0;
    margin: 0;
    text-align: center;
    font-weight: 300;
    text-transform: uppercase;
    line-height: 1;
    text-shadow: 0 2px 8px rgba(0,0,0,0.35);
  }
  .title-line {
    display: flex;
    justify-content: center;
    align-items: center;
  }
  .title-line--first { font-size: 54px; letter-spacing: 1px; }
  .title-line--second { font-size: 64px; margin-top: 6px; }
  .title-stack {
    display: flex;
    flex-direction: column;
    font-size: 24px;
    line-height: 1.05;
    margin-right: 12px;
    text-align: center;
  }
  .title-line--rule { font-size: 58px; margin-top: 10px; }
  .title-rule {
    display: inline-block;
    width: 66px;
    height: 6px;
    background: var(--ink-white);
    margin: 0 22px;
  }
  .title-line--last { font-size: 80px; letter-spacing: 1px; margin-top: 8px; }
  .subtitle {
    position: absolute;
    top: 1042px;
    left: 0;
    right: 0;
    margin: 0;
    text-align: center;
    font-weight: 400;
    font-size: 19px;
    line-height: 1.7;
    letter-spacing: 0.5px;
    text-transform: uppercase;
  }
</style>
</head>
<body>
  <main class="cover">
    <div class="cover-photo" role="img" aria-label="Close-up photograph of a dart striking a red and black target against a pale blue sky"></div>

    <p class="author">Dorian Pelham</p>

    <h1 class="title">
      <span class="title-line title-line--first">Founders</span>
      <span class="title-line title-line--second">
        <span class="title-stack"><span>Behind</span><span>the</span></span>Quiet
      </span>
      <span class="title-line title-line--rule">
        <span class="title-rule"></span>Trade<span class="title-rule"></span>
      </span>
      <span class="title-line title-line--last">Boom</span>
    </h1>

    <p class="subtitle">25 captivating stories of success<br>from discovering hidden opportunities</p>
  </main>
</body>
</html>
```